Upscale beer and food event for Colorado non-profit preserving Lieutenant's Lodge

We need an event poster design that may be incorporated into email invitations. We are a non-profit that helps to preserve an iconic historic building in Colorado. This event celebrates all that is Colorado - especially craft beer and our emerging culinary scene. This event is open to the public. It attracts young professionals...age 30 to 40. You can see our past event design which was done in house...we would like to see something more sophisticated. This year we will need a little room build in for sponsors and committee member names but the other elements are similar...pairings, live music, historic venue, special guest Governor Paul Drenwater, The date is Thursday, August 17th, 2017 from 6:00PM to 8:30m. Early bird tickets start at $55 and go up to 75 on July 13th, 2017. Tickets are available at www.rivetonhearth.example. Contact Marissa Plaut at marissa@vlhtrust.

Target Market(s)

Young professionals, beer and food appreciators, historic preservation supporters

Industry/Entity Type

Non Profit

Colors

Designer to choose colors to be used in the design.

Requirements
Must have
• fresh but elegant feel, think beer at a garden party, nice attire. Focus on Colorado - this event is held at Colorado's "white house" - we refer to it as the valley's hearth. Please be sure that it is clear that the event is hosted by and and benefits the Lieutenant's Lodge Heritage Trust. I can get you a logo but it kinda sucks so just be sure to use the non-profit name. Please include a space for presenting sponsor TRELLWICK SAVINGS CO. We would like to be able to add additional sponsor logos as we go.
Nice to have
• image or sketch of the historic Lieutenant's Lodge at the Quarrington mansion...I have lots of images if you need some high res photos or renderings.
Should not have
• grunge graphics, anything political, it should not be too busy...I like a little white space.

```html
<!DOCTYPE html>
<html lang="en">
<head>
<meta charset="utf-8">
<title>Brews and Bites Pairing 2017</title>
<link href="https://fonts.googleapis.com/css2?family=Barlow+Condensed:wght@300;400;500;600;700&family=Barlow+Semi+Condensed:wght@300;400;600&display=swap" rel="stylesheet">
<style>
  :root{
    --page:#e9e4de;
    --paper:#f6e7db;
    --ink:#111;
    --gold:#c2a35c;
    --gold-soft:#d9c592;
    --mocha:#9a7866;
    --band:#d5bcac;
    --sketch:#b59483;
  }
  html,body{margin:0;width:1200px;height:1200px;overflow:hidden;background:var(--page);}
  .poster{
    position:absolute;left:230px;top:30px;width:884px;height:1364px;
    transform:scale(0.836);transform-origin:top left;
    background:var(--paper);overflow:hidden;
    font-family:"Barlow Semi Condensed","Barlow Condensed",sans-serif;color:var(--ink);
    box-shadow:0 6px 20px rgba(0,0,0,.18);
  }
  .abs{position:absolute;}
  .frame{position:absolute;left:0;top:0;}
  .mansion-sketch{
    position:absolute;left:40px;top:70px;width:790px;height:480px;
    background:radial-gradient(ellipse at 55% 60%, rgba(181,148,131,.45), rgba(181,148,131,.12) 65%, rgba(181,148,131,0) 80%);
  }
  .banner-text{
    position:absolute;left:147px;top:27px;width:575px;height:40px;
    display:flex;align-items:center;justify-content:center;
    font-family:"Barlow Condensed",sans-serif;font-weight:600;font-size:29px;
    letter-spacing:14px;color:var(--paper);
  }
  .title{position:absolute;left:0;width:884px;text-align:center;font-family:"Barlow Condensed",sans-serif;line-height:1;}
  .title-brews{top:112px;font-size:124px;font-weight:700;color:var(--mocha);letter-spacing:1px;}
  .title-and{top:237px;font-size:42px;font-weight:400;}
  .title-bites{top:272px;font-size:200px;font-weight:400;letter-spacing:-2px;}
  .title-pairing{top:455px;font-size:80px;font-weight:300;letter-spacing:20px;padding-left:20px;}
  .emblem{
    position:absolute;width:176px;height:176px;border-radius:50%;
    background:var(--paper);border:6px solid var(--gold-soft);box-sizing:border-box;
    display:flex;align-items:center;justify-content:center;
  }
  .emblem-inner{width:140px;height:140px;border-radius:50%;border:5px solid var(--ink);box-sizing:border-box;
    background:radial-gradient(circle,#d9cfbf 0 38%,#efe6d6 39%);}
  .photo{
    position:absolute;width:220px;height:220px;border-radius:50%;
    border:7px solid var(--gold-soft);box-sizing:border-box;
  }
  .photo-glasses{background:linear-gradient(150deg,#3a4a2a,#8a6a40 55%,#e8e2d6);}
  .photo-lawn{background:linear-gradient(180deg,#9cc0d8,#5f8a4a 50%,#3f6a30);}
  .photo-brewers{background:linear-gradient(160deg,#8a9a50,#c08070 50%,#e6e0d8);}
  .photo-bass{background:linear-gradient(160deg,#6f9a50,#c88a9a 40%,#8a5a44);}
  .photo-garden{background:linear-gradient(180deg,#a8c8d8,#5f8a44 50%,#4a6a3a);}
  .photo-chef{background:linear-gradient(160deg,#8fa27a,#2a3040 50%,#c8b89a);}
  .date{position:absolute;left:0;width:884px;text-align:center;line-height:1;}
  .date-day{top:568px;font-size:52px;font-weight:300;}
  .date-main{top:610px;font-family:"Barlow Condensed",sans-serif;font-size:66px;font-weight:600;color:var(--gold);}
  .date-time{top:676px;font-size:52px;font-weight:300;}
  .details{position:absolute;left:0;width:884px;text-align:center;font-size:29px;font-weight:400;line-height:32px;}
  .label{font-family:"Barlow Condensed",sans-serif;font-weight:600;color:var(--mocha);}
  .fine{position:absolute;left:0;width:884px;top:1033px;text-align:center;font-size:20px;font-weight:300;line-height:23px;}
  .ticket-band{
    position:absolute;left:0;top:1097px;width:884px;height:83px;background:var(--band);
    text-align:center;font-size:20px;line-height:23px;padding-top:8px;box-sizing:border-box;
  }
  .ticket-band b{font-weight:600;}
  .host-name{
    position:absolute;left:352px;top:1240px;width:180px;text-align:center;
    font-size:20px;font-weight:600;line-height:22px;color:var(--ink);
  }
  .sponsor-name{position:absolute;left:552px;top:1236px;font-size:34px;font-weight:400;line-height:36px;}
</style>
</head>
<body>
<div class="poster">
  <div class="mansion-sketch" role="img" aria-label="Faint pencil sketch of the historic Lieutenant's Lodge with trees behind it"></div>

  <svg class="frame" width="884" height="1364" viewBox="0 0 884 1364" aria-hidden="true">
    <!-- top left corner -->
    <path d="M62 32 H150" stroke="#111" stroke-width="6" fill="none"/>
    <path d="M62 32 L78 52 V62" stroke="#111" stroke-width="5" fill="none"/>
    <path d="M40 70 V600" stroke="#111" stroke-width="6"/>
    <path d="M53 80 V580" stroke="#c2a35c" stroke-width="5"/>
    <path d="M25 60 L70 70 L40 82 Z" fill="#c2a35c"/>
    <!-- banner -->
    <path d="M147 27 H722 L740 47 L722 67 H147 L129 47 Z" fill="#c2a35c"/>
    <!-- top right corner -->
    <path d="M720 32 H822" stroke="#111" stroke-width="6" fill="none"/>
    <path d="M822 32 L806 52 V62" stroke="#111" stroke-width="5" fill="none"/>
    <path d="M852 70 V1300" stroke="#111" stroke-width="6"/>
    <path d="M838 80 V1290" stroke="#c2a35c" stroke-width="5"/>
    <path d="M860 60 L815 70 L845 82 Z" fill="#c2a35c"/>
    <path d="M40 600 V1300" stroke="#111" stroke-width="6"/>
    <path d="M53 600 V1290" stroke="#c2a35c" stroke-width="5"/>
    <!-- bottom corners -->
    <path d="M62 1322 H160" stroke="#c2a35c" stroke-width="6"/>
    <path d="M62 1332 H170" stroke="#111" stroke-width="5"/>
    <path d="M30 1298 L78 1310 L50 1330 Z" fill="#111"/>
    <path d="M722 1322 H822" stroke="#c2a35c" stroke-width="6"/>
    <path d="M712 1332 H822" stroke="#111" stroke-width="5"/>
    <path d="M858 1298 L810 1310 L838 1330 Z" fill="#111"/>
    <!-- date arrows -->
    <path d="M222 640 H270" stroke="#111" stroke-width="6"/>
    <path d="M222 652 H270" stroke="#c2a35c" stroke-width="6"/>
    <path d="M262 626 L292 646 L262 666 L272 646 Z" fill="#c2a35c"/>
    <path d="M614 640 H677" stroke="#111" stroke-width="6"/>
    <path d="M614 652 H677" stroke="#c2a35c" stroke-width="6"/>
    <path d="M622 626 L592 646 L622 666 L612 646 Z" fill="#111"/>
    <!-- diamonds -->
    <g transform="translate(442 742)">
      <path d="M0 -12 L16 0 L0 12 L-16 0 Z" fill="#c2a35c"/>
      <path d="M0 -12 L16 0 L0 0 Z M0 12 L-16 0 L0 0 Z" fill="#111"/>
    </g>
    <g transform="translate(442 1010)">
      <path d="M0 -12 L16 0 L0 12 L-16 0 Z" fill="#c2a35c"/>
      <path d="M0 -12 L16 0 L0 0 Z M0 12 L-16 0 L0 0 Z" fill="#111"/>
    </g>
  </svg>

  <div class="banner-text">JOIN US FOR THE 2017</div>

  <div class="title title-brews">BREWS</div>
  <div class="title title-and">and</div>
  <div class="title title-bites">BITES</div>
  <div class="title title-pairing">pairing</div>

  <div class="emblem" style="left:29px;top:279px;"><div class="emblem-inner" role="img" aria-label="Fork and spoon on a plate emblem"></div></div>
  <div class="emblem" style="left:689px;top:279px;"><div class="emblem-inner" role="img" aria-label="Frothy beer mug emblem"></div></div>

  <div class="photo photo-glasses" style="left:-3px;top:542px;" role="img" aria-label="Photo of two snifter glasses of dark beer on a table"></div>
  <div class="photo photo-lawn" style="left:-3px;top:757px;" role="img" aria-label="Photo of guests mingling on the mansion lawn"></div>
  <div class="photo photo-brewers" style="left:-3px;top:1002px;" role="img" aria-label="Photo of brewers standing by a food table"></div>
  <div class="photo photo-bass" style="left:672px;top:542px;" role="img" aria-label="Photo of an upright bass and amplifier in the garden"></div>
  <div class="photo photo-garden" style="left:672px;top:762px;" role="img" aria-label="Photo of a crowd in the garden"></div>
  <div class="photo photo-chef" style="left:672px;top:1002px;" role="img" aria-label="Photo of a chef slicing sandwiches outdoors"></div>

  <div class="date date-day">Thursday</div>
  <div class="date date-main">August 17th</div>
  <div class="date date-time">6:00-8:30pm</div>

  <div class="details" style="top:769px;"><span class="label">LIVE MUSIC</span> by Hollow Fiddle</div>
  <div class="details" style="top:815px;"><span class="label">SPECIAL GUEST</span><br>Governor Paul Drenwater</div>
  <div class="details" style="top:893px;"><span class="label">LOCATION</span><br>Historic Lieutenant's Lodge<br>at the Quarrington Mansion</div>

  <div class="fine">Early bird tickets start at $55<br>and go up to $75 on July 13th, 2017</div>

  <div class="ticket-band">TICKETS ARE AVAILABLE at<br><b>www.rivetonhearth.example</b><br>CONTACT Marissa Plaut at <b>marissa@vlhtrust</b></div>

  <div class="host-name">Lieutenant's Lodge Heritage Trust</div>
  <div class="sponsor-name">TRELLWICK<br>SAVINGS CO</div>
</div>
</body>
</html>
```